Velmoxa AdAgency Presentation

We need ppt design for an ad agency re-branding, agency is based in Moscow, Russia. Our specifics is brand audit, consulting and strategy in web and offline.
We decided to do re-branding because our current agency does not answer the purpose and we need a kind of "second breath".
The idea of re-branding appeared because of many changes that happened in company: new clients, new projects level, new team.
So we'd like to promote company of changes and design should show this spirit as possible.
You may use info in attached pdf file (sorry for Russian language). Info is not so necessary, it will be replaced later.

Please use more colors than digital blue and grey!

Industry/Entity Type

Ad Agency

Requirements
Must have
• Logo is attached. Please choose one.

Ppt project should include:
- Front and last page design
- Heading and list design
- Page-separator design
- Diagram design
- Pics appearance

```html
<!DOCTYPE html>
<html lang="ru">
<head>
<meta charset="utf-8">
<title>Velmoxa — Деятельность компании</title>
<link rel="stylesheet" href="https://fonts.googleapis.com/css2?family=Open+Sans:wdth,wght@75..100,300..700&display=swap">
<style>
  :root {
    --ink-white: #ffffff;
    --subtitle-grey: #9a9a9a;
    --page-grey: #efefef;
    --fold-grey: #8a8a8a;
    --footer-dark: #3b3b3b;
    --accent-blue: #6a9bbf;
    --accent-pink: #ec145f;
    --accent-yellow: #f5cb00;
    --text-dark: #3a2a00;
  }
  * { margin: 0; padding: 0; box-sizing: border-box; }
  html, body { width: 1200px; height: 656px; overflow: hidden; background: #fff; }
  body { font-family: "Open Sans", sans-serif; position: relative; }

  .slide-header {
    position: absolute; left: 0; top: 0; width: 1200px; height: 112px;
    background: linear-gradient(90deg, #5a5a5a 0%, #8a8a8a 25%, #4a4a4a 55%, #2a2a2a 80%, #0e0e0e 100%);
  }
  .slide-title {
    position: absolute; left: 232px; top: 36px;
    font-weight: 300; font-size: 44px; font-stretch: 82%; letter-spacing: -1.5px;
    color: var(--ink-white); line-height: 1;
  }
  .brand {
    position: absolute; left: 904px; top: 28px; width: 66px; text-align: center; color: var(--ink-white);
  }
  .brand-mark { width: 30px; height: 30px; background: var(--ink-white); margin: 0 auto 6px; }
  .brand-name { font-size: 15px; font-weight: 300; font-stretch: 85%; letter-spacing: -0.5px; }

  .lead {
    position: absolute; left: 0; top: 190px; width: 1208px; text-align: center;
    font-weight: 300; font-size: 21px; font-stretch: 86%; letter-spacing: -0.8px; color: var(--subtitle-grey);
  }

  .area-card { position: absolute; top: 249px; width: 178px; height: 238px; }
  .area-card svg { display: block; }
  .area-label {
    position: absolute; left: 14px; top: 64px; width: 150px; text-align: center;
    font-size: 15px; font-stretch: 85%; line-height: 17px; letter-spacing: -0.4px;
    color: var(--ink-white); white-space: nowrap;
    transform: rotate(-26deg);
  }
  .area-label.three-lines { top: 51px; }
  .area-card.is-yellow .area-label { color: var(--text-dark); }

  .slide-footer {
    position: absolute; left: 0; top: 620px; width: 1200px; height: 36px; background: var(--footer-dark);
  }
  .copyright {
    position: absolute; left: 236px; top: 13px; font-size: 8px; font-stretch: 85%; color: #e6e6e6;
  }
  .slide-number {
    position: absolute; left: 865px; top: 0; width: 102px; height: 36px;
    background: var(--accent-pink); color: var(--ink-white);
    font-size: 22px; font-stretch: 85%; letter-spacing: -0.8px; line-height: 36px; text-align: center;
  }
</style>
</head>
<body>
  <header class="slide-header" role="img" aria-label="Затемнённая фотография рабочего процесса команды">
    <h1 class="slide-title">Деятельность компании</h1>
    <div class="brand">
      <div class="brand-mark"></div>
      <div class="brand-name">Velmoxa</div>
    </div>
  </header>

  <p class="lead">Сфера деятельности компании охватывает несколько областей:</p>

  <div class="area-card" style="left:256px;">
    <svg width="178" height="238" viewBox="0 0 178 238">
      <path d="M0,238 V16 Q0,0 16,0 H162 Q178,0 178,16 V178 L118,238 Z" fill="var(--page-grey)"/>
      <g fill="#fff">
        <rect x="14" y="106" width="150" height="5"/><rect x="14" y="119" width="150" height="5"/>
        <rect x="14" y="132" width="150" height="5"/><rect x="14" y="145" width="150" height="5"/>
        <rect x="14" y="158" width="150" height="5"/><rect x="14" y="171" width="150" height="5"/>
        <rect x="14" y="184" width="94" height="5"/><rect x="14" y="197" width="94" height="5"/>
        <rect x="14" y="210" width="94" height="5"/><rect x="14" y="223" width="94" height="5"/>
      </g>
      <path d="M14,24 Q14,14 24,14 H154 Q164,14 164,24 V82 L14,148 Z" fill="var(--accent-blue)"/>
      <path d="M0,154 L178,74 V88 L0,168 Z" fill="#fff"/>
      <path d="M118,178 H178 L118,238 Z" fill="var(--fold-grey)"/>
      <text x="138" y="202" font-family="Open Sans, sans-serif" font-weight="700" font-size="24" fill="#fff" text-anchor="middle">1</text>
    </svg>
    <div class="area-label" style="left:10px;">Производство и<br>медиаразмещение</div>
  </div>

  <div class="area-card" style="left:512px;">
    <svg width="178" height="238" viewBox="0 0 178 238">
      <path d="M0,238 V16 Q0,0 16,0 H162 Q178,0 178,16 V178 L118,238 Z" fill="var(--page-grey)"/>
      <g fill="#fff">
        <rect x="14" y="106" width="150" height="5"/><rect x="14" y="119" width="150" height="5"/>
        <rect x="14" y="132" width="150" height="5"/><rect x="14" y="145" width="150" height="5"/>
        <rect x="14" y="158" width="150" height="5"/><rect x="14" y="171" width="150" height="5"/>
        <rect x="14" y="184" width="94" height="5"/><rect x="14" y="197" width="94" height="5"/>
        <rect x="14" y="210" width="94" height="5"/><rect x="14" y="223" width="94" height="5"/>
      </g>
      <path d="M14,24 Q14,14 24,14 H154 Q164,14 164,24 V82 L14,148 Z" fill="var(--accent-pink)"/>
      <path d="M0,154 L178,74 V88 L0,168 Z" fill="#fff"/>
      <path d="M118,178 H178 L118,238 Z" fill="var(--fold-grey)"/>
      <text x="138" y="202" font-family="Open Sans, sans-serif" font-weight="700" font-size="24" fill="#fff" text-anchor="middle">2</text>
    </svg>
    <div class="area-label three-lines">Маркетинг и<br>стратегическое<br>планирование</div>
  </div>

  <div class="area-card is-yellow" style="left:767px;">
    <svg width="178" height="238" viewBox="0 0 178 238">
      <path d="M0,238 V16 Q0,0 16,0 H162 Q178,0 178,16 V178 L118,238 Z" fill="var(--page-grey)"/>
      <g fill="#fff">
        <rect x="14" y="106" width="150" height="5"/><rect x="14" y="119" width="150" height="5"/>
        <rect x="14" y="132" width="150" height="5"/><rect x="14" y="145" width="150" height="5"/>
        <rect x="14" y="158" width="150" height="5"/><rect x="14" y="171" width="150" height="5"/>
        <rect x="14" y="184" width="94" height="5"/><rect x="14" y="197" width="94" height="5"/>
        <rect x="14" y="210" width="94" height="5"/><rect x="14" y="223" width="94" height="5"/>
      </g>
      <path d="M14,24 Q14,14 24,14 H154 Q164,14 164,24 V82 L14,148 Z" fill="var(--accent-yellow)"/>
      <path d="M0,154 L178,74 V88 L0,168 Z" fill="#fff"/>
      <path d="M118,178 H178 L118,238 Z" fill="var(--fold-grey)"/>
      <text x="138" y="202" font-family="Open Sans, sans-serif" font-weight="700" font-size="24" fill="#fff" text-anchor="middle">3</text>
    </svg>
    <div class="area-label three-lines" style="left:4px;">Разработка<br>творческих и дизайн<br>материалов</div>
  </div>

  <footer class="slide-footer">
    <p class="copyright">©&nbsp;&nbsp;Velmoxa - 2013, All Rights Reserved</p>
    <div class="slide-number">Slide-2</div>
  </footer>
</body>
</html>
```